T SHIRT BUSINESS That needs a Flyer of SERVICES offered (LOGO PROVIDED)

I want a flyer created for my Custom Tshirt Design business (SHIRTS IN BLOOM). I want to be able to hand this to a customer so that they can easily find the info they need about my business to be able to contact me for their custom tshirt needs. I would like to display some of our custom artwork that will entice the buyer to SHOP! This flyer should be colorful and bold but please not clutter. I want it to be very professional looking so that when printed on high quality stock it will be attractive.

Target Market(s)

CUSTOM DESIGN CLOTHING AUDIENCE.

Industry/Entity Type

Clothing

Font styles to use
Decorative

Colors
ec1f27
fbed22
0455a3

Requirements
Must have
• Business Info
Name: SHIRTS IN BLOOM
NUMBER: 555-417-3862
email: shirtsinbloom@mailbox.example
website: shirtsinbloom.example
FB: SHIRTSINBLOOM
Instagram: @shirtsinbloom
Business Description: Design Custom Apparel
Type: DTG and Vinyl Printing
SLOGAN: SHIRTS IN BLOOM - WE KEEP IT LOUD!
PRICING: CUSTOM T-SHIRTS STARING @ $25
Nice to have
• Additional inputs from the designer
Should not have
• Please do not make the flyer cluttered.

```html
<!DOCTYPE html>
<html lang="en">
<head>
<meta charset="utf-8">
<title>Shirts In Bloom – Flyer</title>
<link href="https://fonts.googleapis.com/css2?family=Archivo+Black&family=Open+Sans:wght@400;600;700&display=swap" rel="stylesheet">
<style>
  :root {
    --page-bg: #e9edf2;
    --paper: #ffffff;
    --paper-shade: #eceef1;
    --frame-grey: #d9dce1;
    --frame-lilac: #aeb3dd;
    --blue-deep: #1a5faf;
    --blue-mid: #1f6fc0;
    --blue-sky: #3a97d6;
    --yellow: #fbed22;
    --ink: #1d1d1f;
    --white: #ffffff;
  }
  * { margin: 0; padding: 0; box-sizing: border-box; }
  html, body { width: 1200px; height: 742px; overflow: hidden; }
  body { background: var(--page-bg); position: relative; font-family: "Open Sans", sans-serif; }

  .flyer {
    position: absolute; left: 351px; top: 19px;
    width: 497px; height: 703px; overflow: hidden;
    background: var(--paper);
    box-shadow: 0 6px 22px rgba(20, 40, 80, 0.22);
  }
  .flyer-art { position: absolute; inset: 0; display: block; }

  .brand {
    position: absolute; left: 40px; top: 52px; width: 170px;
    text-align: center; color: var(--white);
  }
  .brand-name { font-weight: 700; font-size: 13px; letter-spacing: 0.5px; line-height: 1; }
  .brand-slogan { font-size: 4.6px; letter-spacing: 0.2px; margin-top: 3px; }

  .offer { position: absolute; left: 23px; top: 405px; color: var(--white); }
  .offer-lead {
    font-family: "Archivo Black", sans-serif; color: var(--yellow);
    font-size: 28px; letter-spacing: 0.5px; line-height: 1;
  }
  .offer-price {
    font-family: "Archivo Black", sans-serif; font-size: 96px;
    line-height: 1; margin-top: 4px; letter-spacing: -1px;
  }

  .about {
    position: absolute; left: 23px; top: 550px; width: 320px;
    color: var(--white); font-size: 11.6px; line-height: 15.6px;
  }

  .contact {
    position: absolute; right: 14px; top: 602px; list-style: none;
    color: var(--ink); font-size: 11.3px; text-align: right;
  }
  .contact li { display: flex; justify-content: flex-end; align-items: center; gap: 5px; height: 21.5px; }
  .contact svg { width: 14px; height: 14px; flex: none; }
</style>
</head>
<body>
  <article class="flyer">
    <svg class="flyer-art" viewBox="0 0 497 703" xmlns="http://www.w3.org/2000/svg">
      <defs>
        <linearGradient id="paperWash" x1="0" y1="0" x2="1" y2="1">
          <stop offset="0" stop-color="#ffffff"/>
          <stop offset="1" stop-color="#e4e6ea"/>
        </linearGradient>
        <linearGradient id="tileTone" x1="0" y1="0" x2="1" y2="1">
          <stop offset="0" stop-color="#3a2a24"/>
          <stop offset="0.5" stop-color="#141416"/>
          <stop offset="1" stop-color="#6b3a1e"/>
        </linearGradient>
        <linearGradient id="tileToneWarm" x1="0" y1="0" x2="1" y2="1">
          <stop offset="0" stop-color="#7a1f1c"/>
          <stop offset="1" stop-color="#1b1b1e"/>
        </linearGradient>
      </defs>

      <rect class="paper-wash" width="497" height="703" fill="url(#paperWash)"/>

      <!-- frame diamonds behind gallery -->
      <rect x="120" y="180" width="300" height="300" rx="40" transform="rotate(45 270 330)" fill="var(--paper-shade)" stroke="var(--frame-grey)" stroke-width="26"/>
      <rect x="105" y="165" width="330" height="330" rx="44" transform="rotate(45 270 330)" fill="none" stroke="var(--frame-lilac)" stroke-width="4"/>

      <!-- header swoosh -->
      <path class="swoosh-light" d="M0 60 C 40 110, 120 120, 210 80 L 210 95 C 120 135, 40 125, 0 80 Z" fill="var(--blue-sky)"/>
      <path class="swoosh-line" d="M0 92 C 50 130, 130 125, 200 100" fill="none" stroke="var(--blue-sky)" stroke-width="2"/>
      <path class="header-badge" d="M40 0 L 210 0 C 210 60, 175 98, 125 98 C 75 98, 40 60, 40 0 Z" fill="var(--blue-deep)"/>
      <circle cx="125" cy="35" r="13" fill="none" stroke="var(--white)" stroke-width="2.2"/>

      <!-- bottom bands -->
      <polygon class="band-deep" points="0,338 300,338 497,440 497,575 365,575 190,395 0,395" fill="var(--blue-mid)"/>
      <polygon class="band-sky" points="0,395 190,395 365,575 265,703 0,703" fill="var(--blue-sky)"/>

      <!-- artwork gallery -->
      <g class="gallery">
        <rect role="img" aria-label="Custom printed black tee with gold lettering" x="339" y="0" width="100" height="100" rx="14" transform="rotate(45 389 50)" fill="url(#tileTone)" stroke="var(--white)" stroke-width="4"/>
        <rect role="img" aria-label="Custom printed tees with red graphic art on display" x="258" y="72" width="106" height="106" rx="14" transform="rotate(45 311 125)" fill="url(#tileToneWarm)" stroke="var(--white)" stroke-width="4"/>
        <rect role="img" aria-label="Custom printed tee with bright red flame artwork" x="401" y="102" width="106" height="106" rx="14" transform="rotate(45 454 155)" fill="url(#tileToneWarm)" stroke="var(--white)" stroke-width="4"/>
        <rect role="img" aria-label="Custom printed tee with motorcycle graphic" x="159" y="165" width="110" height="110" rx="14" transform="rotate(45 214 220)" fill="url(#tileTone)" stroke="var(--white)" stroke-width="4"/>
        <rect role="img" aria-label="Black tee with orange and white snake artwork" x="274" y="230" width="190" height="190" rx="22" transform="rotate(45 369 325)" fill="url(#tileTone)" stroke="var(--white)" stroke-width="5"/>
      </g>
    </svg>

    <header class="brand">
      <div class="brand-name">SHIRTS IN BLOOM</div>
      <div class="brand-slogan">SHIRTS IN BLOOM - WE KEEP IT LOUD!</div>
    </header>

    <section class="offer">
      <div class="offer-lead">STARING</div>
      <div class="offer-price">$25</div>
    </section>

    <p class="about">We are a business that is dedicated to meeting your printing needs. We specialize in Direct To Garment (DTG) and Vinyl printing services on a variety of garments Bringing our customers custom design ideas to life is our passion. Custom Tees.</p>

    <ul class="contact">
      <li>555-417-3862
        <svg viewBox="0 0 16 16"><circle cx="8" cy="8" r="7" fill="none" stroke="#1d1d1f" stroke-width="1.5"/><path d="M5.2 4.3l1.4-.3.8 1.8-.9.7c.5 1.1 1.2 1.8 2.3 2.3l.7-.9 1.8.8-.3 1.4c-3 .2-6-2.8-5.8-5.8z" fill="#1d1d1f"/></svg>
      </li>
      <li>shirtsinbloom.example
        <svg viewBox="0 0 16 16" fill="none" stroke="#1d1d1f" stroke-width="1.3"><circle cx="8" cy="8" r="7"/><ellipse cx="8" cy="8" rx="3" ry="7"/><path d="M1 8h14M2.2 4.5h11.6M2.2 11.5h11.6"/></svg>
      </li>
      <li>SHIRTSINBLOOM
        <svg viewBox="0 0 16 16"><circle cx="8" cy="8" r="7" fill="none" stroke="#1d1d1f" stroke-width="1.5"/></svg>
      </li>
      <li>@shirtsinbloom
        <svg viewBox="0 0 16 16"><rect x="1.5" y="1.5" width="13" height="13" rx="3" fill="none" stroke="#1d1d1f" stroke-width="1.5"/></svg>
      </li>
    </ul>
  </article>
</body>
</html>
```